Www.zapdeck.com monthly sweepstakes.

Every month I am giving away 1st place $500 gift card to your local RC hobby shop of choice, 2nd place $100 gift card 3rd place ZapDeck merch. All things rc: cars, boats, quadcopters, helicopters, airplanes.

Needs to be with the color theme of the website. Check zapdeck.com for current sweepstakes banner. New banner should be half the size in height. I will post dimension later.

Target Market(s)

Rc hobbies cars airplanes helicopters boats

Industry/Entity Type

RemoteControl hobbies

Requirements
Must have
• 1440x680 size, Blend with black background, creative and in incorporate all trypes of rc craft
Should not have
• To many different colors, dosnt need logo as its already on website. This is a banner for my homepage

```html
<!DOCTYPE html>
<html lang="en">
<head>
<meta charset="UTF-8">
<title>ZapDeck Monthly Sweepstakes Banner</title>
<link href="https://fonts.googleapis.com/css2?family=Montserrat:wght@700;800&family=Lato:wght@700&family=Playfair+Display:wght@700&display=swap" rel="stylesheet">
<style>
  :root {
    --page-bg: #ffffff;
    --night: #141414;
    --night-soft: #242628;
    --accent-red: #e8201c;
    --text-white: #ffffff;
    --heli-red: #d9211b;
    --yacht-white: #eef0f2;
    --truck-yellow: #f2c21a;
    --truck-dark: #1d1d1d;
  }
  * { margin: 0; padding: 0; box-sizing: border-box; }
  html, body {
    width: 1200px; height: 1000px; overflow: hidden;
    background: var(--page-bg);
  }
  .canvas { position: relative; width: 1200px; height: 1000px; }
  .banner {
    position: absolute; left: 10px; top: 221px;
    width: 1180px; height: 557px; overflow: hidden;
    background: var(--night);
  }
  .skyline-backdrop {
    position: absolute; inset: 0;
    background:
      linear-gradient(180deg, rgba(20,20,20,0) 0%, rgba(20,20,20,0) 55%, rgba(10,10,10,0.85) 100%),
      radial-gradient(ellipse at 60% 70%, #2e3134 0%, var(--night-soft) 40%, var(--night) 80%);
  }
  .flight-path { position: absolute; left: 0; top: 0; }
  .photo-helicopter {
    position: absolute; left: 80px; top: 15px; width: 385px; height: 205px;
    border-radius: 90px 120px 40px 60px;
    background: radial-gradient(ellipse at 60% 45%, #ef3a2f 0%, var(--heli-red) 55%, #8a130f 100%);
  }
  .photo-yacht {
    position: absolute; left: 28px; top: 440px; width: 487px; height: 115px;
    border-radius: 60px 20px 10px 80px;
    background: linear-gradient(180deg, #d8dcdf 0%, var(--yacht-white) 50%, #bfc4c8 100%);
  }
  .photo-truck {
    position: absolute; left: 823px; top: 362px; width: 292px; height: 178px;
    border-radius: 50px 50px 60px 60px;
    background: linear-gradient(180deg, var(--truck-yellow) 0%, #d9a912 40%, var(--truck-dark) 70%, #2b2b2b 100%);
  }
  .prize-box {
    position: absolute; left: 769px; top: 30px; width: 371px; height: 174px;
    border: 2px solid var(--accent-red); border-radius: 20px;
    text-align: center; color: var(--text-white);
    font-family: 'Montserrat', sans-serif; font-weight: 800;
    padding-top: 26px;
  }
  .prize-box .rank { color: var(--accent-red); font-size: 38px; line-height: 44px; }
  .prize-box .amount { font-size: 36px; line-height: 46px; }
  .prize-box .amount .value { color: var(--accent-red); }
  .prize-box .where {
    font-family: 'Lato', sans-serif; font-weight: 700;
    font-size: 20px; line-height: 36px;
  }
  sup { font-size: 0.5em; vertical-align: 0.9em; line-height: 0; }
  .headline {
    position: absolute; left: 187px; top: 245px; width: 830px;
    font-family: 'Playfair Display', serif; font-weight: 700;
    font-size: 51px; letter-spacing: 1px; color: var(--text-white);
    white-space: nowrap; line-height: 60px;
  }
  .headline .win { color: var(--accent-red); }
  .runner-up-list {
    position: absolute; left: 342px; top: 322px; list-style: none;
    font-family: 'Montserrat', sans-serif; font-weight: 700;
    font-size: 33px; color: var(--text-white);
  }
  .runner-up-list li { display: flex; align-items: center; height: 49px; white-space: nowrap; }
  .runner-up-list .arrow { width: 24px; height: 24px; margin-right: 12px; }
  .runner-up-list .red { color: var(--accent-red); }
</style>
</head>
<body>
<div class="canvas">
  <section class="banner">
    <div class="skyline-backdrop" role="img" aria-label="Dark night city skyline photograph"></div>

    <svg class="flight-path" width="300" height="360" viewBox="0 0 300 360" aria-hidden="true">
      <path d="M215 208 C170 262 95 280 55 255 C20 232 30 180 80 172 C140 165 165 215 150 260 C135 310 70 350 0 352"
            fill="none" stroke="#ffffff" stroke-width="2" stroke-dasharray="7 6"/>
    </svg>

    <div class="photo-helicopter" role="img" aria-label="Red RC helicopter"></div>
    <div class="photo-yacht" role="img" aria-label="White RC yacht"></div>
    <div class="photo-truck" role="img" aria-label="Yellow and black RC monster truck"></div>

    <div class="prize-box">
      <div class="rank">1<sup>ST</sup> PLACE</div>
      <div class="amount"><span class="value">$500</span> GIFT CARD</div>
      <div class="where">To Your Local Hobby Shop</div>
    </div>

    <h1 class="headline"><span class="win">WIN</span> AN RC SHOPPING SPREE!</h1>

    <ul class="runner-up-list">
      <li>
        <svg class="arrow" viewBox="0 0 24 24" aria-hidden="true"><path d="M2 3 L22 12 L2 21 L7 12 Z" fill="#e8201c"/></svg>
        <span><span class="red">2<sup>ND</sup></span>&nbsp;Place <span class="red">$100</span> Gift Card</span>
      </li>
      <li>
        <svg class="arrow" viewBox="0 0 24 24" aria-hidden="true"><path d="M2 3 L22 12 L2 21 L7 12 Z" fill="#e8201c"/></svg>
        <span><span class="red">3<sup>RD</sup></span>&nbsp;Place <span class="red">ZapDeck Merch</span></span>
      </li>
    </ul>
  </section>
</div>
</body>
</html>
```